Sports League Registration Banner for facebook

I have a graphic with a basic idea for an ad that I would like to post on facebook but I need it to be reconfigured to fit their dimensions (1194 by 624, or in that ratio) and to have the text moved and placed in another spot on the ad. I also want the colors to be changed to look like my website (www.pkvathletics.com) but no logo on the ad. This is to promote registration for a sports league.

The idea is basically to get up off the couch and play some sports. The text on the bottom should be moved off to the side and replaced with:

GET FIT HAVE FUN
10 Game Season + Playoffs
1 Game per week
Team Fee $1525
Player Fee $125

Men's Ball Hockey

Industry/Entity Type

Graphic Design

```html
<!DOCTYPE html>
<html lang="en">
<head>
<meta charset="utf-8">
<title>Get Fit Have Fun – League Registration Banner</title>
<link rel="stylesheet" href="https://fonts.googleapis.com/css2?family=Croissant+One&family=Cinzel:wght@900&family=Margarine&family=Play:wght@400;700&display=swap">
<style>
  :root {
    --page-bg: #ffffff;
    --banner-green: #8abb4d;
    --frame-white: #f4f8ee;
    --ink: #111111;
    --accent-orange: #f7921e;
    --accent-purple: #6a2d8f;
    --bubble-pink: #ec6b94;
    --reg-green: #4e8a1c;
    --sticker-green: #7fb546;
    --photo-dark: #2a1c14;
    --photo-mid: #6b4530;
    --photo-warm: #b07a55;
  }
  * { margin: 0; padding: 0; box-sizing: border-box; }
  html, body {
    width: 1200px;
    height: 961px;
    overflow: hidden;
    background: var(--page-bg);
  }
  .banner {
    position: absolute;
    left: 105px;
    top: 222px;
    width: 990px;
    height: 517px;
    background: var(--banner-green);
    box-shadow: 2px 3px 4px rgba(0,0,0,0.35);
    overflow: hidden;
  }
  .photo-frame {
    position: absolute;
    left: 5px;
    top: 5px;
    width: 742px;
    height: 505px;
    border: 3px solid var(--frame-white);
    border-radius: 34px;
    padding: 4px;
  }
  .photo-frame::before {
    content: "";
    position: absolute;
    left: 190px; right: 190px; top: -5px;
    border-top: 2px dashed var(--frame-white);
  }
  .photo-frame::after {
    content: "";
    position: absolute;
    top: 150px; bottom: 150px; left: -5px;
    border-left: 2px dashed var(--frame-white);
  }
  .couch-photo {
    width: 100%;
    height: 100%;
    border-radius: 28px;
    background:
      radial-gradient(ellipse at 35% 70%, var(--photo-warm) 0%, transparent 45%),
      radial-gradient(ellipse at 80% 40%, #5d605a 0%, transparent 30%),
      linear-gradient(160deg, var(--photo-mid) 0%, var(--photo-dark) 60%, #1a120d 100%);
  }
  .sticker {
    position: absolute;
    left: 517px;
    top: 95px;
    width: 146px;
    height: 146px;
  }
  .sticker svg { position: absolute; inset: 0; overflow: visible; }
  .sticker-text {
    position: absolute;
    inset: 0;
    text-align: center;
    font-family: "Croissant One", "Georgia", serif;
    line-height: 1;
    white-space: nowrap;
  }
  .sticker-top {
    display: block;
    margin-top: 18px;
    color: var(--accent-purple);
    font-size: 24px;
    transform: rotate(-8deg);
  }
  .sticker-small {
    display: block;
    margin-top: 12px;
    color: #fff;
    font-size: 15px;
    -webkit-text-stroke: 1px #333;
    paint-order: stroke fill;
  }
  .sticker-big {
    display: block;
    color: #fff;
    font-size: 28px;
    -webkit-text-stroke: 2px #333;
    paint-order: stroke fill;
    transform: rotate(-6deg);
  }
  .offer {
    position: absolute;
    left: 752px;
    top: 0;
    width: 236px;
    height: 517px;
    text-align: center;
  }
  .offer > * {
    position: absolute;
    left: 0;
    right: 0;
    line-height: 1;
    white-space: nowrap;
  }
  .headline {
    font-family: "Croissant One", "Georgia", serif;
    font-weight: 400;
    -webkit-text-stroke: 3px var(--ink);
    paint-order: stroke fill;
  }
  .headline-fit { top: 22px; font-size: 44px; color: #fff; }
  .headline-fun { top: 103px; font-size: 40px; color: var(--accent-orange); }
  .season {
    top: 180px;
    font-family: "Cinzel", serif;
    font-weight: 900;
    font-size: 24px;
    color: var(--ink);
  }
  .plus {
    top: 204px;
    font-family: "Play", sans-serif;
    font-size: 20px;
    color: var(--ink);
  }
  .playoffs {
    top: 219px;
    font-family: "Croissant One", "Georgia", serif;
    font-size: 25px;
    color: var(--accent-purple);
  }
  .weekly {
    top: 262px;
    font-family: "Cinzel", serif;
    font-weight: 900;
    font-size: 20px;
    color: var(--ink);
    -webkit-text-stroke: 3px #fff;
    paint-order: stroke fill;
  }
  .weekly .num { color: var(--accent-orange); }
  .fee {
    font-family: "Margarine", cursive;
    font-size: 33px;
    color: var(--ink);
    -webkit-text-stroke: 3px #fff;
    paint-order: stroke fill;
  }
  .fee .price { color: var(--accent-purple); }
  .fee-team { top: 303px; }
  .fee-player { top: 353px; }
  .register {
    top: 412px;
    left: 10px;
    right: 4px;
    height: 76px;
  }
  .register svg { position: absolute; inset: 0; }
  .register-text {
    position: absolute;
    top: 19px;
    left: 0; right: 0;
    font-family: "Play", sans-serif;
    font-size: 18px;
    color: var(--reg-green);
  }
  .site {
    top: 494px;
    left: 19px;
    text-align: left;
    font-family: "Play", sans-serif;
    font-weight: 700;
    font-size: 14px;
    color: var(--ink);
  }
</style>
</head>
<body>
  <section class="banner">
    <div class="photo-frame">
      <div class="couch-photo" role="img" aria-label="Photo of a man lounging on a worn couch holding a beer mug and a burger, an old television and radio in a dim brick room"></div>
    </div>

    <div class="sticker">
      <svg viewBox="0 0 146 146" aria-hidden="true">
        <defs>
          <clipPath id="disc"><circle cx="73" cy="73" r="70"/></clipPath>
        </defs>
        <circle cx="73" cy="73" r="70" fill="var(--sticker-green)" stroke="#ffffff" stroke-width="3"/>
        <path d="M0 0 H146 V60 L0 78 Z" fill="#ffffff" clip-path="url(#disc)"/>
        <circle cx="73" cy="73" r="70" fill="none" stroke="var(--sticker-green)" stroke-width="4"/>
        <circle cx="18" cy="138" r="7" fill="var(--sticker-green)"/>
        <circle cx="8" cy="152" r="4" fill="var(--sticker-green)"/>
      </svg>
      <div class="sticker-text">
        <span class="sticker-top">IT'S<br>NEVER</span>
        <span class="sticker-small">TOO</span>
        <span class="sticker-big">LATE</span>
      </div>
    </div>

    <div class="offer">
      <h1 class="headline headline-fit">GET FIT</h1>
      <h2 class="headline headline-fun">HAVE FUN</h2>
      <p class="season">10 Game Season</p>
      <p class="plus">+</p>
      <p class="playoffs">Playoffs</p>
      <p class="weekly"><span class="num">1</span> Game per week</p>
      <p class="fee fee-team">Team Fee <span class="price">$1525</span></p>
      <p class="fee fee-player">Player Fee <span class="price">$125</span></p>
      <div class="register">
        <svg viewBox="0 0 222 76" aria-hidden="true">
          <path d="M32 62 L22 76 L48 66 Z" fill="#ffffff" stroke="var(--bubble-pink)" stroke-width="5" stroke-linejoin="round"/>
          <ellipse cx="111" cy="36" rx="106" ry="32" fill="#ffffff" stroke="var(--bubble-pink)" stroke-width="6"/>
          <path d="M30 58 L25 72 L46 63 Z" fill="#ffffff"/>
        </svg>
        <p class="register-text">Registration before</p>
      </div>
      <p class="site">www.pkvathletics.com</p>
    </div>
  </section>
</body>
</html>
```